Te Pakaraki Team

We need a poster designed to capture the Mission, Objective, Values and Behaviours of a new project team.

"Te Pakaraki" is Maori for "first". This team is responsible for delivering the first Light Rail Line for Auckland and there will be many firsts required to achieve the project objectives.

Mission - Auckland loves light rail
Objective - to shift the behaviours of Aucklanders so that they use the Light Rail and love it once it is developed
Values and Behaviours as per attachmen

The poster needs to incorporate the essence of some of the images in the paintings in the attached document, in particular the yellow tram / light rail image with the thumbs up to be in the poster somewhere.

It is important to continue to incorporate Maori into our everyday language.

```html
<!DOCTYPE html>
<html lang="en">
<head>
<meta charset="UTF-8">
<title>Te Pakaraki Team – Auckland Loves Light Rail</title>
<link href="https://fonts.googleapis.com/css2?family=Anton&family=Montserrat:wght@600;700;800&display=swap" rel="stylesheet">
<style>
  :root {
    --green: #1a9a3f;
    --green-bright: #22b95a;
    --green-dark: #12802f;
    --red: #d2262b;
    --ink: #151515;
    --text: #2d2d2d;
    --stage: #e8e8e8;
    --white: #ffffff;
  }
  * { margin: 0; padding: 0; box-sizing: border-box; }
  html, body { width: 1200px; height: 1200px; overflow: hidden; background: var(--stage); }
  .canvas { position: relative; width: 1200px; height: 1200px; }
  .poster {
    position: absolute; left: 177px; top: 0; width: 846px; height: 1200px;
    background: var(--white); overflow: hidden;
    font-family: "Montserrat", Arial, sans-serif;
  }
  .poster-art { position: absolute; inset: 0; }
  .title {
    position: absolute; left: 66px; top: 72px;
    font-family: "Anton", "Impact", sans-serif; font-size: 70px; line-height: 1;
    color: var(--ink); letter-spacing: -0.5px; white-space: nowrap;
  }
  .title-rule { position: absolute; left: 66px; top: 152px; width: 440px; height: 2px; background: #d8d2bd; }
  .mission { position: absolute; left: 64px; top: 164px; color: var(--text); font-weight: 800; }
  .mission span { display: block; line-height: 1; }
  .mission .m-city { font-size: 37px; }
  .mission .m-loves { font-size: 72px; color: var(--red); margin-top: 6px; letter-spacing: -1px; }
  .mission .m-rail { font-size: 43px; margin-top: 10px; }
  .values-card {
    position: absolute; left: 66px; top: 887px; width: 714px; height: 285px;
    background: linear-gradient(160deg, #ffffff 0%, #f3f3f3 100%);
    border-radius: 26px; box-shadow: 0 4px 14px rgba(0,0,0,0.12);
  }
  .roll-tab {
    position: absolute; left: 53px; top: 916px; width: 287px; height: 50px;
    background: var(--green); color: var(--white); border-radius: 0 12px 12px 0;
    font-weight: 700; font-size: 28px; line-height: 50px; padding-left: 42px;
    box-shadow: 0 6px 8px rgba(0,0,0,0.15);
  }
  .value { position: absolute; width: 300px; }
  .value-icon {
    position: absolute; left: -74px; top: -2px; width: 60px; height: 60px;
    border: 2px solid #3a3a3a; border-radius: 50%; background: var(--white);
    display: flex; align-items: center; justify-content: center;
  }
  .value-title { font-size: 16.5px; font-weight: 700; color: var(--green); line-height: 1.2; }
  .value-text { font-size: 16px; font-weight: 600; color: var(--text); line-height: 1.15; margin-top: 3px; white-space: nowrap; }
</style>
</head>
<body>
<div class="canvas">
  <div class="poster">
    <svg class="poster-art" width="846" height="1200" viewBox="0 0 846 1200">
      <defs>
        <linearGradient id="greySweep" x1="0" y1="0" x2="1" y2="1">
          <stop offset="0" stop-color="#eef0f4"/>
          <stop offset="1" stop-color="#c9ccd8"/>
        </linearGradient>
        <linearGradient id="greyLeft" x1="0" y1="0" x2="1" y2="0">
          <stop offset="0" stop-color="#c8cbd7"/>
          <stop offset="1" stop-color="#f6f6f8"/>
        </linearGradient>
        <radialGradient id="paperA" cx="0.6" cy="0.4" r="0.7">
          <stop offset="0" stop-color="#efe58a"/>
          <stop offset="0.45" stop-color="#e9e7da"/>
          <stop offset="1" stop-color="#dcdfd2"/>
        </radialGradient>
        <radialGradient id="paperB" cx="0.5" cy="0.5" r="0.6">
          <stop offset="0" stop-color="#c9332f"/>
          <stop offset="0.3" stop-color="#e6b83a"/>
          <stop offset="0.6" stop-color="#e8dfb8"/>
          <stop offset="1" stop-color="#eeece8"/>
        </radialGradient>
        <radialGradient id="paperC" cx="0.4" cy="0.5" r="0.65">
          <stop offset="0" stop-color="#d63a2a"/>
          <stop offset="0.25" stop-color="#e4b0a2"/>
          <stop offset="0.65" stop-color="#ece6dc"/>
          <stop offset="1" stop-color="#dcd8d0"/>
        </radialGradient>
      </defs>

      <path d="M630 0 Q 720 250 846 430 L846 0 Z" fill="url(#greySweep)"/>
      <path d="M540 0 L640 0 Q 720 260 846 440 L846 500 Q 690 300 540 0 Z" fill="var(--green-bright)"/>
      <path d="M0 540 Q 420 470 846 430 L846 510 Q 420 510 0 600 Z" fill="var(--green-bright)"/>
      <path d="M0 600 Q 200 560 330 560 L 120 800 Q 50 820 0 900 Z" fill="url(#greyLeft)"/>
      <path d="M0 860 Q 50 760 130 700 L150 715 Q 60 800 0 900 Z" fill="var(--green)"/>
      <rect x="0" y="1100" width="846" height="100" fill="var(--green)"/>

      <circle cx="519" cy="358" r="172" fill="var(--white)" stroke="var(--green)" stroke-width="4"/>
      <circle cx="519" cy="358" r="158" fill="url(#paperA)" role="img" aria-label="Child's painting of a smiling yellow light rail train giving a thumbs up over the city"/>

      <circle cx="280" cy="639" r="212" fill="var(--green)"/>
      <circle cx="280" cy="639" r="196" fill="var(--white)"/>
      <circle cx="280" cy="639" r="190" fill="url(#paperB)" role="img" aria-label="Child's painting of a city skyline, a train, a rainbow and a heart"/>

      <circle cx="583" cy="613" r="172" fill="var(--white)" stroke="var(--green)" stroke-width="4"/>
      <circle cx="583" cy="613" r="160" fill="url(#paperC)" role="img" aria-label="Child's painting of a red heart, a city tower and a blue light rail train"/>
    </svg>

    <div class="title">TE PAKARAKI TEAM</div>
    <div class="title-rule"></div>
    <div class="mission">
      <span class="m-city">AUCKLAND</span>
      <span class="m-loves">LOVES</span>
      <span class="m-rail">LIGHT RAIL</span>
    </div>

    <div class="values-card"></div>
    <div class="roll-tab">HOW WE ROLL</div>

    <div class="value" style="left:181px; top:1002px;">
      <div class="value-icon">
        <svg width="30" height="30" viewBox="0 0 30 30"><path d="M15 22 C6 15 4 11 7 7 C10 4 13 6 15 9 C17 6 20 4 23 7 C26 11 24 15 15 22 Z" fill="var(--green)"/><path d="M3 25 L10 21 L18 24 L27 19" stroke="var(--green)" stroke-width="2.5" fill="none" stroke-linecap="round"/></svg>
      </div>
      <div class="value-title">INTEGRITY AND HONESTY</div>
      <div class="value-text">Build trust through being<br>a true voice</div>
    </div>

    <div class="value" style="left:179px; top:1086px;">
      <div class="value-icon">
        <svg width="32" height="32" viewBox="0 0 32 32"><path d="M2 12 L9 9 L16 13 L23 9 L30 12 L30 19 L23 22 L18 26 L14 23 L9 20 L2 19 Z" fill="var(--green)"/><path d="M11 18 L15 21 M14 16 L18 19 M17 14 L21 17" stroke="var(--white)" stroke-width="1.5"/></svg>
      </div>
      <div class="value-title">RESPECT</div>
      <div class="value-text">Be empathetic, listen and<br>support team choices</div>
    </div>

    <div class="value" style="left:501px; top:919px;">
      <div class="value-icon">
        <svg width="30" height="30" viewBox="0 0 30 30"><path d="M15 26 C4 18 2 12 5 8 C8 4 13 5 15 9 C17 5 22 4 25 8 C28 12 26 18 15 26 Z" fill="var(--green)"/><path d="M15 11 V20 M10.5 15.5 H19.5" stroke="var(--white)" stroke-width="2.5"/></svg>
      </div>
      <div class="value-title">CARE</div>
      <div class="value-text">Understanding the what, why<br>and how we impact on people</div>
    </div>

    <div class="value" style="left:498px; top:1002px;">
      <div class="value-icon">
        <svg width="30" height="30" viewBox="0 0 30 30"><rect x="5" y="13" width="5" height="12" fill="var(--green)"/><path d="M12 13 L16 5 C18 5 19 7 18 10 L24 10 C26 10 27 12 26 14 L24 23 C23 25 22 25 20 25 L12 25 Z" fill="var(--green)"/><path d="M15 1 V3 M20 2 L19 4 M10 2 L11 4" stroke="var(--green)" stroke-width="1.5"/></svg>
      </div>
      <div class="value-title">COMMITTED</div>
      <div class="value-text">to the project deliverables,<br>values and behaviors</div>
    </div>

    <div class="value" style="left:501px; top:1086px;">
      <div class="value-icon">
        <svg width="30" height="30" viewBox="0 0 30 30"><circle cx="14" cy="8" r="5" fill="none" stroke="var(--green)" stroke-width="2.2"/><path d="M3 27 C3 19 8 16 14 16 C17 16 19 17 21 18" fill="none" stroke="var(--green)" stroke-width="2.2"/><circle cx="21" cy="23" r="5.5" fill="none" stroke="var(--green)" stroke-width="2"/><path d="M21 20 V26 M18 23 H24" stroke="var(--green)" stroke-width="2"/></svg>
      </div>
      <div class="value-title">BE BOLD</div>
      <div class="value-text">Challenge convention<br>while having fun</div>
    </div>
  </div>
</div>
</body>
</html>
```